2 guided dives on the North of Bonaire

2 guided shore dives on the North of Bonaire including authentic local lunch and drinks.
We offer an adventure for experienced divers to discover the dive sites on the north of the island.
Showing you the beauty of the reefs and tasting authentic local cuisine like goat or iguana combined with a stunning view of the surroundings.

Target Market(s)

Divers / tourism

Industry/Entity Type

Tourism / Diving

Font styles to use
Sans Serif

Colors
0054AA
0677BA
7BADD7
CADEEF
E8F1F8
0094D4
00A9DD
6FCCEA
C7EBF8
E9F6FB
F0912C
F2A743
F7CA91
FBE8D2
FDF5EE
EE7325
F08F49
F5BC92
FAE3D3
FDF4ED

Requirements
Must have
• Some of the pictures I uploaded and the food picture / bottom like in the pictures
Nice to have
• inviting to join us on the guided dives
Should not have
• Any picture I didn't provide

```html
<!DOCTYPE html>
<html lang="en">
<head>
<meta charset="utf-8">
<title>Let Us Guide You – Guided Dives North Bonaire</title>
<link rel="stylesheet" href="https://fonts.googleapis.com/css2?family=Montserrat:wght@500;600;700;800;900&display=swap">
<style>
:root{
  --navy:#0b2a55;
  --deep-blue:#0054AA;
  --blue:#0677BA;
  --sky:#7BADD7;
  --ice:#E8F1F8;
  --cyan:#00A9DD;
  --aqua:#6FCCEA;
  --orange:#F0912C;
  --orange-dark:#EE7325;
  --orange-light:#F2A743;
  --white:#ffffff;
}
*{margin:0;padding:0;box-sizing:border-box}
html,body{width:800px;height:1200px;overflow:hidden;background:var(--white)}
body{font-family:'Montserrat',Arial,sans-serif}
.flyer{position:relative;width:800px;height:1200px;overflow:hidden;background:var(--navy)}
.hero-photo{position:absolute;left:0;top:0;width:800px;height:620px;
  background:linear-gradient(180deg,#5f8fbf 0%,#8fb6d8 30%,#3c7a6a 52%,#1f6f9a 70%,#0f4f86 100%)}
.hero-shade{position:absolute;left:0;top:0;width:800px;height:620px;
  background:linear-gradient(180deg,rgba(11,42,85,.35) 0%,rgba(11,42,85,0) 45%,rgba(11,42,85,.55) 100%)}
.partner-badge{position:absolute;right:48px;top:44px;width:92px;height:92px;border-radius:50%;background:var(--deep-blue);border:5px solid var(--white)}
.headline{position:absolute;left:54px;top:46px;font-weight:900;line-height:.98;font-size:104px;letter-spacing:-1px;text-transform:uppercase}
.headline .accent{color:var(--orange)}
.headline .main{color:var(--white)}
.offer{position:absolute;left:0;right:0;top:300px;text-align:center}
.offer-title{display:inline-block;background:var(--orange);color:var(--white);font-weight:800;font-size:44px;padding:10px 40px;text-transform:uppercase;letter-spacing:.5px}
.offer-sub{display:block;margin:0 auto;width:460px;background:var(--deep-blue);color:var(--white);font-weight:600;font-size:19px;padding:8px 0;text-transform:uppercase;letter-spacing:1px}
.swoosh{position:absolute;left:0;top:430px;width:800px;height:200px}
.gallery{position:absolute;left:86px;top:510px;width:628px;display:grid;grid-template-columns:1fr 1fr;gap:20px}
.photo{height:190px;border:6px solid var(--white);box-shadow:0 4px 10px rgba(0,0,0,.35)}
.photo-coast{background:linear-gradient(180deg,#8fc3e6 0%,#4aa6c9 45%,#b9a37a 75%,#8a7a55 100%)}
.photo-beach{background:linear-gradient(180deg,#9fd0ef 0%,#39b3d6 45%,#e9dcc0 100%)}
.photo-shore{background:linear-gradient(180deg,#a9d6f2 0%,#22a5cf 55%,#f1e6cc 100%)}
.photo-food{background:radial-gradient(circle at 50% 50%,#e7b25a 0%,#b86b2a 45%,#5c3a1e 100%)}
.perks{position:absolute;left:86px;top:946px;width:628px;display:flex;justify-content:space-between}
.perk{display:flex;align-items:center;gap:12px;color:var(--white);font-size:17px;font-weight:600;width:300px;line-height:1.25}
.perk svg{flex:none}
.lunch{position:absolute;left:86px;top:1018px;width:628px;text-align:center;color:var(--white);font-weight:700;font-size:22px;padding:8px 0;border-top:2px solid var(--orange);border-bottom:2px solid var(--orange)}
.footer{position:absolute;left:60px;right:60px;top:1090px;display:flex;align-items:center;justify-content:space-between}
.brand{display:flex;align-items:center;gap:12px;color:var(--white);font-weight:800;font-size:26px}
.brand .dot{width:38px;height:38px;border-radius:50%;background:var(--orange)}
.contacts{display:flex;flex-direction:column;gap:10px;align-items:flex-end}
.pill{background:var(--orange);color:var(--white);font-weight:700;font-size:19px;padding:8px 22px;border-radius:24px;display:flex;align-items:center;gap:10px}
.pill.web{background:var(--orange-dark)}
</style>
</head>
<body>
<div class="flyer">
  <div class="hero-photo" role="img" aria-label="Coastal view of the north side of Bonaire with blue sea and green cliffs"></div>
  <div class="hero-shade"></div>
  <div class="partner-badge" aria-hidden="true"></div>

  <h1 class="headline"><span class="accent">Let us</span><br><span class="main">Guide you!</span></h1>

  <div class="offer">
    <div class="offer-title">2 Guided Dives</div>
    <span class="offer-sub">At the north side of Bonaire</span>
  </div>

  <svg class="swoosh" viewBox="0 0 800 200" preserveAspectRatio="none" aria-hidden="true">
    <path d="M0 70 Q400 -10 800 70 L800 200 L0 200 Z" fill="var(--white)"/>
    <path d="M0 84 Q400 6 800 84 L800 200 L0 200 Z" fill="var(--navy)"/>
  </svg>

  <div class="gallery">
    <div class="photo photo-coast" role="img" aria-label="Rocky coastline with turquoise water"></div>
    <div class="photo photo-beach" role="img" aria-label="Shore dive entry on a sandy beach"></div>
    <div class="photo photo-shore" role="img" aria-label="Palm-shaded beach by clear blue sea"></div>
    <div class="photo photo-food" role="img" aria-label="Plate of authentic local Bonaire cuisine"></div>
  </div>

  <div class="perks">
    <div class="perk">
      <svg width="30" height="30" viewBox="0 0 30 30" aria-hidden="true"><circle cx="15" cy="15" r="14" fill="var(--orange)"/><path d="M8 15.5l4.5 4.5L22 10.5" stroke="var(--white)" stroke-width="3" fill="none" stroke-linecap="round"/></svg>
      We show you the best stuff
    </div>
    <div class="perk">
      <svg width="30" height="30" viewBox="0 0 30 30" aria-hidden="true"><circle cx="15" cy="15" r="14" fill="var(--orange)"/><path d="M8 15.5l4.5 4.5L22 10.5" stroke="var(--white)" stroke-width="3" fill="none" stroke-linecap="round"/></svg>
      You just enjoy the dive, we take care of the rest
    </div>
  </div>

  <div class="lunch">Authentic Local Lunch And Drinks At Casa Vista Alta</div>

  <div class="footer">
    <div class="brand"><span class="dot"></span>Reefline Dive</div>
    <div class="contacts">
      <div class="pill">
        <svg width="18" height="18" viewBox="0 0 24 24" aria-hidden="true"><path d="M6.6 10.8a15 15 0 006.6 6.6l2.2-2.2a1 1 0 011-.25 11.4 11.4 0 003.6.57 1 1 0 011 1V20a1 1 0 01-1 1A17 17 0 013 4a1 1 0 011-1h3.5a1 1 0 011 1c0 1.25.2 2.45.57 3.6a1 1 0 01-.25 1z" fill="var(--white)"/></svg>
        Call us: +599 700 1234
      </div>
      <div class="pill web">Visit us: www.reeflinedive.com</div>
    </div>
  </div>
</div>
</body>
</html>
```